Hausverwaltung von Wohnimmobilien sucht Corporate Design
Die Kommunikation und Zusammenarbeit war ausgezeichnet. Wir sind sehr glücklich ein passendes Logo gefunden zu haben. Änderungen wurden sehr schnell und unkompliziert umgesetzt. Malte Orvisek versteht seinen Job - immer wieder gern!
Zielgruppe
Hausverwaltung von Wohnimmobilien, Mietverwaltung für private Eigentümer von Mehrfamilienhäuser in Berlin . Wir suchen ein klassisches und zeitloses Design mit modernen Aspekten.
Aufgabenstellung
Design soll Vertrauen, Tradition und Kompetenz ausstrahlen. Wir sind ein Traditionsunternehmen, dass sich im Umbruch befindet. Wir übernehmen das Unternehmen und wollen neuen Schwung und Moderne einfließen lassen, jedoch sollen die traditionellen Werte erhalten bleiben.

```html
<!DOCTYPE html>
<html lang="de">
<head>
<meta charset="utf-8">
<title>Immobilienverwaltung Konrad Wessel – Corporate Design</title>
<link href="https://fonts.googleapis.com/css2?family=Montserrat:wght@600&family=Open+Sans:wght@400;600&family=PT+Sans:ital,wght@1,700&display=swap" rel="stylesheet">
<style>
:root{
  --brand:#456990;
  --ink:#4B4B4D;
  --paper:#ffffff;
  --bg:#e6e7e9;
  --window:#cccccc;
  --text:#3a3a3a;
}
*{margin:0;padding:0;box-sizing:border-box}
html,body{width:1200px;height:494px;overflow:hidden;background:var(--bg)}
body{position:relative;font-family:"Open Sans",sans-serif;color:var(--text)}
.piece{position:absolute;background:var(--paper);overflow:hidden}
.band{position:absolute;left:0;right:0;bottom:0;background:var(--brand)}

/* wordmark */
.wordmark{position:absolute;text-align:center;font-family:"Montserrat",sans-serif;font-weight:600;color:var(--brand);line-height:1}
.wordmark .mark{display:block;margin:0 auto;background:var(--brand)}
.wordmark .name{display:block;white-space:nowrap}
.wordmark .owner{display:block;white-space:nowrap}
.wordmark.on-brand{color:var(--paper)}
.wordmark.on-brand .mark{background:var(--paper)}

/* stickers */
.sticker{position:absolute;width:36px;height:36px;border-radius:50%;display:flex;align-items:center;justify-content:center;font-family:"Montserrat",sans-serif;font-weight:600;font-size:9px}
.sticker.light{left:121px;top:40px;background:var(--paper);color:var(--brand)}
.sticker.dark{left:169px;top:40px;background:var(--brand);color:var(--paper)}

/* cd */
.disc{position:absolute;left:169px;top:114px;width:122px;height:122px;border-radius:50%;background:var(--brand)}
.disc::after{content:"";position:absolute;left:-8px;top:52px;width:18px;height:18px;border-radius:50%;background:var(--bg)}
.sleeve{left:104px;top:112px;width:126px;height:126px}

/* contact lists */
.contact{position:absolute;list-style:none;line-height:1.3}
.contact li{position:relative;padding-left:1.8em;white-space:nowrap}
.contact li.icon::before{content:"";position:absolute;left:0;top:.3em;width:.75em;height:.75em;background:var(--ink);border-radius:1px}

/* cards */
.card-front{left:355px;top:105px;width:117px;height:70px}
.card-back{left:483px;top:105px;width:117px;height:70px;background:var(--brand)}
.card-person{position:absolute;left:6px;top:31px;font-size:4.3px;text-decoration:underline;color:var(--ink)}
.card-contact{font-size:2.8px;top:39px}

/* envelopes */
.env-front{left:41px;top:269px;width:273px;height:129px}
.env-contact{font-size:4.3px;top:84px}
.env-window{position:absolute;left:178px;top:76px;width:70px;height:39px;border-radius:4px;background:var(--window)}
.env-back{left:329px;top:269px;width:273px;height:129px}

/* letterhead */
.letter{left:660px;top:54px;width:242px;height:344px}
.sender{position:absolute;left:23px;top:69px;font-size:3.6px;line-height:1.3}
.letter-contact{font-size:3.6px;left:176px;top:68px;line-height:1.15}
.subject{position:absolute;left:23px;top:107px;width:120px;font-size:3.6px;line-height:1.35}
.subject dt{float:left;width:21px;clear:left}
.subject dd{white-space:nowrap}
.body-copy{position:absolute;left:23px;top:133px;width:200px;font-size:3.4px;line-height:1.45;text-align:justify}
.body-copy p{margin-bottom:4.5px}
.body-copy p:first-child{text-indent:10px}
.footer-bank{font-size:3.6px;left:23px;top:303px}
.footer-id{font-size:3.6px;left:120px;top:303px}
.director{position:absolute;left:191px;top:296px;font-size:3.8px;font-weight:600}
.signature{position:absolute;left:180px;top:310px}

/* folder */
.folder{left:916px;top:55px;width:243px;height:344px;background:var(--brand)}
.folder-spine{position:absolute;left:11px;top:0;bottom:0;width:2px;background:#1e2a38}

/* palette */
.palette-title{position:absolute;left:511px;top:426px;width:178px;text-align:center;font-family:"PT Sans",sans-serif;font-style:italic;font-weight:700;font-size:17px;color:var(--ink)}
.swatch{position:absolute;top:449px;height:7px;width:89px}
.swatch.brand{left:511px;background:var(--brand)}
.swatch.ink{left:600px;background:var(--ink)}
.hex{position:absolute;top:463px;width:89px;text-align:center;font-family:"PT Sans",sans-serif;font-style:italic;font-weight:700;font-size:14px;color:var(--ink)}
</style>
</head>
<body>

<div class="sticker light">KW</div>
<div class="sticker dark">KW</div>

<div class="disc"></div>
<div class="piece sleeve">
  <div class="wordmark" style="left:0;right:0;top:48px">
    <span class="mark" style="width:10px;height:10px;margin-bottom:6px"></span>
    <span class="name" style="font-size:16px">WESSEL</span>
  </div>
</div>

<div class="piece card-front">
  <div class="wordmark" style="left:6px;top:12px;text-align:left">
    <span class="name" style="font-size:4.3px">IMMOBILIENVERWALTUNG</span>
    <span class="owner" style="font-size:2.4px;letter-spacing:1.2px;margin-top:1px">KONRAD WESSEL</span>
  </div>
  <div class="card-person">jan berger</div>
  <ul class="contact card-contact" style="left:6px">
    <li class="icon">www.hv-wessel.de</li>
    <li class="icon">lindenauer str. 14,<br>10999 Berlin</li>
  </ul>
  <ul class="contact card-contact" style="left:63px">
    <li class="icon">jan.berger@hv-wessel.de</li>
    <li class="icon">030 - 481 72 15 / 16<br>030 - 481 72 19</li>
  </ul>
  <div class="band" style="height:3px"></div>
</div>

<div class="piece card-back">
  <div class="wordmark on-brand" style="left:0;right:0;top:26px">
    <span class="mark" style="width:6px;height:6px;margin-bottom:4px"></span>
    <span class="name" style="font-size:4.3px">IMMOBILIENVERWALTUNG</span>
    <span class="owner" style="font-size:2.4px;letter-spacing:1.2px;margin-top:1px">KONRAD WESSEL</span>
  </div>
</div>

<div class="piece env-front">
  <div class="wordmark" style="left:14px;top:26px;width:92px">
    <span class="mark" style="width:8px;height:8px;margin-bottom:5px"></span>
    <span class="name" style="font-size:6px">IMMOBILIENVERWALTUNG</span>
    <span class="owner" style="font-size:3px;letter-spacing:1.6px;margin-top:1.5px">KONRAD WESSEL</span>
  </div>
  <ul class="contact env-contact" style="left:14px">
    <li class="icon">www.hv-wessel.de</li>
    <li class="icon">lindenauer str. 14,<br>10999 Berlin</li>
  </ul>
  <ul class="contact env-contact" style="left:94px">
    <li class="icon">jan.berger@hv-wessel.de</li>
    <li class="icon">030 - 481 72 15 / 16<br>030 - 481 72 19</li>
  </ul>
  <div class="env-window"></div>
  <div class="band" style="height:6px"></div>
</div>

<div class="piece env-back">
  <svg width="273" height="129" viewBox="0 0 273 129" aria-hidden="true">
    <polygon points="0,0 273,0 273,20 136,65 0,20" fill="var(--brand)"/>
  </svg>
  <div class="band" style="height:6px"></div>
</div>

<div class="piece letter">
  <div class="wordmark" style="left:130px;top:27px;width:94px">
    <span class="mark" style="width:8px;height:8px;margin-bottom:5px"></span>
    <span class="name" style="font-size:6px">IMMOBILIENVERWALTUNG</span>
    <span class="owner" style="font-size:3px;letter-spacing:1.6px;margin-top:1.5px">KONRAD WESSEL</span>
  </div>
  <div class="sender">konrad wessel e.k.<br>hausverwaltungen, Lindenauer str.<br>14, 10999 Berlin</div>
  <ul class="contact letter-contact">
    <li class="icon">lindenauer str. 14,<br>10999 Berlin</li>
    <li class="icon">030 - 481 72 15 / 16<br>030 - 481 72 19</li>
    <li class="icon">info@hv-wessel.de</li>
    <li class="icon">www.hv-wessel.de</li>
  </ul>
  <dl class="subject">
    <dt>Lorem</dt><dd>: Ipsum dolor sit amet</dd>
    <dt>Consectu</dt><dd>: -</dd>
    <dt>Elit</dt><dd>: sed diam nonummy nibh euismod</dd>
  </dl>
  <div class="body-copy">
    <p>Lorem ipsum dolor sit amet, consectetuer adipiscing elit, sed diam nonummy nibh euismod tincidunt ut laoreet dolore magna aliquam erat volutpat. Ut wisi enim ad minim veniam, quis nostrud exerci tation ullamcorper suscipit lobortis nisl ut aliquip ex ea commodo consequat. Duis autem vel eum iriure dolor in hendrerit in vulputate velit esse molestie consequat, vel illum dolore eu feugiat nulla facilisis at vero eros et accumsan et iusto odio dignissim qui blandit praesent luptatum zzril delenit augue duis dolore te feugait nulla facilisi. Nam liber tempor cum soluta nobis eleifend option congue nihil imperdiet doming id quod mazim placerat facer possim assum.</p>
    <p>Typi non habent claritatem insitam; est usus legentis in iis qui facit eorum claritatem. Investigationes demonstraverunt lectores legere me lius quod ii legunt saepius. Claritas est etiam processus dynamicus, qui sequitur mutationem consuetudium lectorum. Eodem modo typi, qui nunc nobis videntur parum clari.</p>
    <p>Typi non habent claritatem insitam; est usus legentis in iis qui facit eorum claritatem. Investigationes demonstraverunt lectores legere me lius quod ii legunt saepius. Claritas est etiam processus dynamicus, qui sequitur mutationem consuetudium lectorum. Eodem modo typi, qui nunc nobis videntur parum clari.</p>
  </div>
  <div class="director">Director</div>
  <svg class="signature" width="40" height="8" viewBox="0 0 40 8" aria-hidden="true">
    <path d="M1 4 C3 1 5 6 7 4 S11 2 13 5 L39 4" fill="none" stroke="var(--text)" stroke-width=".6"/>
  </svg>
  <ul class="contact footer-bank">
    <li class="icon">IBAN: DE00 0000 0000 0000 00<br>BIC: WSSLDEB1XXX</li>
  </ul>
  <ul class="contact footer-id">
    <li class="icon">19/100/100/100</li>
  </ul>
  <div class="band" style="height:10px"></div>
</div>

<div class="piece folder">
  <div class="folder-spine"></div>
  <div class="wordmark on-brand" style="left:60px;right:0;top:150px">
    <span class="mark" style="width:12px;height:12px;margin-bottom:8px"></span>
    <span class="name" style="font-size:22px">WESSEL</span>
  </div>
</div>

<div class="palette-title">color palette</div>
<div class="swatch brand"></div>
<div class="swatch ink"></div>
<div class="hex" style="left:511px">#456990</div>
<div class="hex" style="left:600px">#4B4B4D</div>

</body>
</html>
```